Recruitment Firm Business Card

I need to design my business cards for my new recruitment company, Brightpath Staffing.

I already have the logo and colours, so half work is already done.

I would like the back of the cards just to be the black background version of the logo...so all black with the logo in the middle.

For the front of the cards I would like it to be white with the small white background version of the logo and the following information:

Maris Kotter
Brightpath Staffing
Managing Director | Application Development Specialist
-----------------------------------------------------------------------

p | +61 2 8156 3042 e | maris@brightpathstaffing.com.au
m | +61 (0)438714926 w | www.brightpathstaffing.com.au

Tarrow Bank Tower
Level 14/ 8 Penhale Street
Sydney, NSW 2000

In terms of how this information is presented I am flexible and open to ideas.

Just please stick to the colour theme - light blue, black and white and make as professional as possible.

```html
<!DOCTYPE html>
<html lang="en">
<head>
<meta charset="utf-8">
<title>Brightpath Staffing – Business Card</title>
<link rel="stylesheet" href="https://fonts.googleapis.com/css2?family=Open+Sans:wght@300;400;600&display=swap">
<style>
  :root {
    --page: #e4e4e4;
    --card-dark: #252525;
    --card-dark-edge: #1c1c1c;
    --brand-blue: #2f8fd6;
    --text-light: #f2f2f2;
    --text-muted: #c9c9c9;
    --text-dim: #8e8e8e;
  }
  * { box-sizing: border-box; margin: 0; padding: 0; }
  html, body {
    width: 1200px; height: 740px; overflow: hidden;
    background: var(--page);
    font-family: "Open Sans", Arial, sans-serif;
  }
  .sheet { position: relative; width: 1200px; height: 740px; }

  .card {
    position: absolute; top: 205px; width: 540px; height: 330px;
    background: radial-gradient(ellipse at 50% 45%, #2c2c2c 0%, var(--card-dark) 55%, var(--card-dark-edge) 100%);
    box-shadow: 0 10px 24px rgba(0,0,0,0.22);
    overflow: hidden; color: var(--text-light);
  }
  .card--back { left: 40px; }
  .card--front { left: 620px; }

  /* brand lockup */
  .brand { position: absolute; display: flex; align-items: center; gap: 14px; }
  .brand__dot {
    width: 46px; height: 46px; border-radius: 50%;
    border: 4px solid var(--brand-blue);
  }
  .brand__name {
    font-weight: 300; color: var(--text-light); line-height: 1.02;
    letter-spacing: 0.5px; text-transform: lowercase;
  }
  .card--back .brand { left: 50%; top: 50%; transform: translate(-50%, -50%); }
  .card--back .brand__name { font-size: 34px; }
  .card--front .brand { left: 32px; top: 142px; }
  .card--front .brand__dot { width: 36px; height: 36px; border-width: 3px; }
  .card--front .brand__name { font-size: 26px; }

  /* back card rules */
  .rule { position: absolute; left: 0; right: 0; background: var(--brand-blue); }
  .card--back .rule { bottom: 18px; height: 5px; }
  .back__web {
    position: absolute; right: 22px; bottom: 30px;
    font-size: 9px; color: var(--text-dim); letter-spacing: 0.3px;
  }

  /* front card header */
  .header {
    position: absolute; left: 0; top: 0; width: 318px; height: 86px;
    background: var(--brand-blue); padding: 16px 22px;
  }
  .header__name { font-size: 22px; font-weight: 400; color: #fff; }
  .header__firm { font-size: 10px; color: #eaf4fc; margin-top: 4px; }
  .header__role { font-size: 9.5px; color: #eaf4fc; margin-top: 2px; }
  .header__street {
    position: absolute; left: 334px; top: 36px;
    font-size: 12px; color: var(--text-light);
  }
  .card--front .rule--top { top: 92px; height: 4px; }
  .card--front .rule--bottom { bottom: 12px; height: 5px; }

  /* contacts */
  .contacts {
    position: absolute; right: 24px; top: 128px;
    list-style: none; text-align: right;
    font-size: 11px; line-height: 20px; color: var(--text-muted);
  }
  .contacts li { display: flex; justify-content: flex-end; align-items: center; gap: 8px; }
  .contacts svg { width: 11px; height: 11px; fill: var(--text-light); flex: none; }
  .contacts .gap { height: 8px; }
</style>
</head>
<body>
<div class="sheet">

  <section class="card card--back" aria-label="Card back">
    <div class="brand">
      <span class="brand__dot"></span>
      <span class="brand__name">brightpath<br>staffing</span>
    </div>
    <span class="back__web">www.brightpathstaffing.com.au</span>
    <div class="rule"></div>
  </section>

  <section class="card card--front" aria-label="Card front">
    <header class="header">
      <h1 class="header__name">Maris Kotter</h1>
      <p class="header__firm">Brightpath Staffing</p>
      <p class="header__role">Managing Director | Application Development Specialist</p>
    </header>
    <p class="header__street">Level 14/ 8 Penhale Street</p>
    <div class="rule rule--top"></div>

    <div class="brand">
      <span class="brand__dot"></span>
      <span class="brand__name">brightpath<br>staffing</span>
    </div>

    <ul class="contacts">
      <li>+61 2 8156 3042
        <svg viewBox="0 0 12 12"><path d="M3 1 L5 3.6 L4 4.8 Q5.2 7 7.2 8 L8.4 7 L11 9 L9.8 11 Q4.5 10.5 1 2.2 Z"/></svg></li>
      <li>+61 (0)438714926
        <svg viewBox="0 0 12 12"><rect x="3" y="0.5" width="6" height="11" rx="1"/><rect x="4" y="2" width="4" height="7" fill="#252525"/></svg></li>
      <li>maris@brightpathstaffing.com.au
        <svg viewBox="0 0 12 12"><rect x="0.5" y="2" width="11" height="8"/><path d="M0.5 2 L6 7 L11.5 2" stroke="#252525" stroke-width="1.2" fill="none"/></svg></li>
      <li>www.brightpathstaffing.com.au
        <svg viewBox="0 0 12 12"><circle cx="6" cy="6" r="5.2"/><path d="M1 6 H11 M6 1 Q3 6 6 11 Q9 6 6 1" stroke="#252525" stroke-width="0.9" fill="none"/></svg></li>
      <li class="gap"></li>
      <li>Tarrow Bank Tower
        <svg viewBox="0 0 12 12"><path d="M6 11.5 Q1.5 6.5 1.5 4.5 A4.5 4.5 0 0 1 10.5 4.5 Q10.5 6.5 6 11.5 Z"/><circle cx="6" cy="4.5" r="1.6" fill="#252525"/></svg></li>
      <li>Sydney, NSW 2000</li>
    </ul>

    <div class="rule rule--bottom"></div>
  </section>

</div>
</body>
</html>
```